Lumaform website scandinavian interior design

Existing website: http://lumaform-example.no/

Webdesign for interior designer Ragna Tvedtholm. The company name is Lumaform. Scandinavian interiør is known to be simple and elegant. The website will be in Norwegian, we are working on the text. The website needs to have a few more pages than just the front page. Here are the different titles of the pages:

1. Hjem
2. Om Lumaform
3. Tjenester og priser
4.. Kontakt oss

There should be Facebook and Instagram icons somewhere at the bottom of the website.

The logo we want to use is attached (pink with black print, see attachment )

We have attached images for inspiration. We want to use some of these colors. The color in the logo, The style should be elegant, modern and delicate.

It is imprtant that the website is user friendly.

Target Market(s)

People who want to decorate their home
Companies and public sector who need to redecorate

Industry/Entity Type

Interior Designer

Coding

Coded - Design and coding required

Number of Pages Required

5+ page

Font styles to use
Other font styles liked:
• see example in the logo breakdown

Requirements
Must have
• Elegant, modern and delicate design
Images of design, see examples attached
Colors similar to the pictures
Should not have
• Too bright colors
Pictures of people

```html
<!DOCTYPE html>
<html lang="en">
<head>
<meta charset="utf-8">
<title>Lumaform – Scandinavian interior design</title>
<link rel="stylesheet" href="https://fonts.googleapis.com/css2?family=Crimson+Pro:wght@400&family=Inter:wght@400;500&display=swap">
<style>
  :root{
    --blush:#e8cfc4;
    --ink:#1c1c1c;
    --text:#4a4a4a;
    --muted:#8c8c8c;
    --pill:#a8a8a8;
    --card-grey:#dedede;
    --line:#9a9a9a;
    --icon:#6b6b6b;
    --serif:"Crimson Pro", Georgia, serif;
    --sans:"Inter", Helvetica, Arial, sans-serif;
  }
  *{box-sizing:border-box;margin:0;padding:0}
  html,body{width:784px;height:1200px;overflow:hidden;background:#fff}
  .page{position:relative;width:784px;height:1200px;font-family:var(--sans);color:var(--text)}
  .abs{position:absolute}

  .brand{left:98px;top:0;width:49px;height:57px;background:var(--blush);display:flex;align-items:center;justify-content:center;font-family:var(--serif);font-size:10px;color:var(--ink)}
  .nav{left:199px;top:12px;display:flex;align-items:center;gap:0;font-size:7.5px;color:var(--ink);height:12px}
  .nav a{color:inherit;text-decoration:none}
  .nav .home{margin-right:13px}
  .nav .suppliers{margin-right:8px}
  .pill{display:inline-flex;align-items:center;justify-content:center;border-radius:20px;font-family:var(--sans);text-decoration:none;line-height:1}
  .pill-outline{border:1px solid var(--pill);color:var(--pill);background:#fff}
  .pill-solid{background:var(--pill);color:#fff}
  .nav .pill{height:11px;font-size:6.5px}
  .nav .demo{width:61px;margin-right:6px}
  .nav .signup{width:38px;margin-right:8px}

  .photo{display:block}
  .hero-photo{left:427px;top:0;width:357px;height:318px;background:linear-gradient(180deg,#5f6064 0%,#8a8b8f 55%,#7a5a3c 85%,#5b4330 100%)}
  .hero-title{left:99px;top:140px;font-family:var(--serif);font-size:27px;line-height:22.7px;color:var(--ink);letter-spacing:-0.3px}

  .cta{display:flex;gap:18px}
  .cta .pill{height:14px;font-size:8.5px}
  .cta .demo{width:73px}
  .cta .signin{width:37px}
  .hero-cta{left:99px;top:252px}

  .about-photo{left:98px;top:367px;width:219px;height:292px;background:linear-gradient(160deg,#eef0f2 0%,#d9dde1 60%,#a9afb5 100%)}
  .eyebrow{left:358px;top:366px;font-size:9px;color:var(--text)}
  .about-title{left:356px;top:376px;font-family:var(--serif);font-size:23.5px;line-height:23.7px;color:var(--ink)}
  .service{width:110px}
  .service h3{font-weight:400;font-size:10.8px;color:#3c3c3c;letter-spacing:.2px;margin-bottom:2px}
  .service p{font-size:6.5px;line-height:7.3px;color:var(--muted);padding-left:2px}
  .s1{left:356px;top:461px;width:80px}
  .s2{left:469px;top:461px}
  .s3{left:357px;top:528px;width:96px}
  .s4{left:469px;top:528px;width:96px}
  .about-cta{left:356px;top:618px}

  .divider{left:49px;top:682px;width:686px;height:1px;background:var(--line)}
  .spec-title{left:94px;top:706px;font-family:var(--serif);font-size:26px;color:#3a3a3a}

  .card{top:759px;height:196px;padding:0}
  .card.grey{background:var(--card-grey)}
  .card .img{position:absolute;top:2px;height:98px}
  .card h3{position:absolute;top:103px;font-weight:400;font-size:11.8px;line-height:12.5px;color:#3a3a3a}
  .card h3.small{font-size:8px;line-height:10.5px;top:108px}
  .card p{position:absolute;font-size:6.8px;line-height:10.7px;color:var(--text)}
  .card .more{position:absolute;top:178px;height:12px;width:43px;font-size:5.8px;border:1px solid #555;color:#333;background:transparent}
  .c1{left:98px;width:142px}
  .c2{left:243px;width:147px}
  .c3{left:395px;width:143px}
  .c4{left:539px;width:147px}
  .c1 .img{left:0;width:142px;background:linear-gradient(180deg,#f1dfd6,#e7cdbf)}
  .c2 .img{left:2px;width:143px;background:linear-gradient(135deg,#d7dce2,#9aa2ac 55%,#2d3138)}
  .c3 .img{left:0;width:142px;background:linear-gradient(180deg,#d9d6d4,#eeebea)}
  .c4 .img{left:3px;width:142px;background:linear-gradient(180deg,#c9cccf 0%,#dadcdd 50%,#9a9a95 100%)}
  .c1 h3,.c1 p,.c1 .more{left:-1px}
  .c1 p{left:0;top:121px}
  .c2 h3,.c2 p,.c2 .more{left:2px}
  .c2 p{top:132px}
  .c3 h3,.c3 p,.c3 .more{left:-1px}
  .c3 p{left:0;top:121px}
  .c3 .more{left:0}
  .c4 h3,.c4 p,.c4 .more{left:4px}
  .c4 p{top:132px}

  .spec-cta{left:328px;top:984px}

  .footer{left:0;top:1029px;width:784px;height:171px;background:var(--blush)}
  .footer h4{font-weight:500;font-size:9.8px;color:#555;letter-spacing:.2px}
  .contact{left:100px;top:1063px}
  .address{left:100px;top:1082px;font-size:9px;line-height:10.2px;color:#555}
  .address .gap{height:10px}
  .follow{left:630px;top:1081px}
  .social{left:514px;top:1101px;display:flex;gap:19px}
  .social span{display:block;width:28px;height:28px;border-radius:50%;background:var(--icon)}
</style>
</head>
<body>
<div class="page">

  <div class="abs brand">Lumaform</div>

  <nav class="abs nav">
    <a class="home" href="#">Home</a>
    <a class="suppliers" href="#">Suppliers</a>
    <a class="pill pill-outline demo" href="#">Book a Demo</a>
    <a class="pill pill-solid signup" href="#">Sign up</a>
    <a href="#">Login</a>
  </nav>

  <div class="abs photo hero-photo" role="img" aria-label="Dining table with a small bonsai tree and white modern chairs against a grey wall"></div>

  <h1 class="abs hero-title" style="font-weight:400">Finding the optimal<br>solutions for a<br>project, whether<br>it is a room or more ...</h1>

  <div class="abs cta hero-cta">
    <a class="pill pill-outline demo" href="#">Book a Demo</a>
    <a class="pill pill-solid signin" href="#">sign in</a>
  </div>

  <div class="abs photo about-photo" role="img" aria-label="Black wireframe cube sculptures with hanging bulbs seen from below"></div>

  <p class="abs eyebrow">Work with us</p>
  <h2 class="abs about-title" style="font-weight:400">Using professional expertise<br>we design through various<br>aproach like</h2>

  <div class="abs service s1">
    <h3>FLOOR PLANS</h3>
    <p>Lorem ipsum dolor<br>sit amet, consecte-<br>tur adipiscing elit,<br>sed do eiusmod<br>tempor incididunt ut<br>labore et dolore</p>
  </div>
  <div class="abs service s2">
    <h3>FURNITURE PLANS</h3>
    <p>Lorem ipsum dolor sit amet, con-<br>sectetur adipiscing elit, sed do<br>eiusmod tempor incididunt ut<br>labore et dolore magna aliqua.<br>Quis ipsum suspendisse ultrices<br>gravida. Risus commodo viverra</p>
  </div>
  <div class="abs service s3">
    <h3>3D DRAWINGS</h3>
    <p>Lorem ipsum dolor sit amet,<br>consectetur adipiscing elit,<br>sed do eiusmod tempor<br>incididunt ut labore et<br>dolore magna aliqua. Quis<br>ipsum suspendisse ultrices</p>
  </div>
  <div class="abs service s4">
    <h3>COLLAGES</h3>
    <p>Lorem ipsum dolor sit amet,<br>consectetur adipiscing elit,<br>sed do eiusmod tempor<br>incididunt ut labore et<br>dolore magna aliqua. Quis<br>ipsum suspendisse ultrices</p>
  </div>

  <div class="abs cta about-cta">
    <a class="pill pill-outline demo" href="#">Book a Demo</a>
    <a class="pill pill-solid signin" href="#">sign in</a>
  </div>

  <div class="abs divider"></div>

  <h2 class="abs spec-title" style="font-weight:400">We are Specialized in</h2>

  <article class="abs card c1">
    <div class="img" role="img" aria-label="Wooden wall shelves with plants and hanging bulbs on a pink wall"></div>
    <h3>Plan for Lighting</h3>
    <p>Lorem ipsum dolor sit amet, consec-<br>tetur adipiscing elit, sed do eiusmod<br>tempor incididunt ut labore et dolore<br>magna aliqua. Quis ipsum suspendis-<br>se ultrices gravida. Risus commodo</p>
    <a class="pill more" href="#">read more</a>
  </article>

  <article class="abs card grey c2">
    <div class="img" role="img" aria-label="Geometric triangular facade panels in grey and black"></div>
    <h3>Interior &amp; Exterior<br>design</h3>
    <p>Lorem ipsum dolor sit amet, consecte-<br>tur adipiscing elit, sed do eiusmod<br>tempor incididunt ut labore et dolore</p>
    <a class="pill more" href="#">read more</a>
  </article>

  <article class="abs card c3">
    <div class="img" role="img" aria-label="Single dark green wooden chair in a pale empty room"></div>
    <h3>Furniture Plan</h3>
    <p>Lorem ipsum dolor sit amet, consec-<br>tetur adipiscing elit, sed do eiusmod<br>tempor incididunt ut labore et dolore<br>magna aliqua. Quis ipsum suspendis-<br>se ultrices gravida. Risus commodo</p>
    <a class="pill more" href="#">read more</a>
  </article>

  <article class="abs card grey c4">
    <div class="img" role="img" aria-label="Small wooden cabin on stilts by a frosty shore"></div>
    <h3 class="small">Space design for<br>Cabins</h3>
    <p>Lorem ipsum dolor sit amet, consecte-<br>tur adipiscing elit, sed do eiusmod<br>tempor incididunt ut labore et dolore</p>
    <a class="pill more" href="#">read more</a>
  </article>

  <div class="abs cta spec-cta">
    <a class="pill pill-outline demo" href="#">Book a Demo</a>
    <a class="pill pill-solid signin" href="#">sign in</a>
  </div>

  <footer class="abs footer"></footer>
  <h4 class="abs contact footer-heading" style="position:absolute">CONTACT</h4>
  <address class="abs address" style="font-style:normal">
    Post / visit address<br>
    Lumaform AS v / Ragna Tvedtholm<br>
    Lyngbakken 14<br>
    3490 Klokkarstua
    <div class="gap"></div>
    Tel. +4790000000<br>
    Mail. post@lumaform-example.no<br>
    Web. www.lumaform-example.no
  </address>
  <h4 class="abs follow" style="position:absolute">FIND US ON</h4>
  <div class="abs social" aria-label="Social media links">
    <span aria-label="Social link 1"></span>
    <span aria-label="Social link 2"></span>
    <span aria-label="Social link 3"></span>
    <span aria-label="Social link 4"></span>
  </div>

</div>
</body>
</html>
```